Corporate Design für Steuerkanzlei
Zielgruppe
Wir sind eine Steuerkanzlei im (ländlichen) Neustadt an der Donau, die seit über 30 Jahren von Herrn Konrad (Vater) Wimmler geführt wird. Mit Einstieg durch Herrn Felix (Sohn) Wimmler haben wir die Wimmler Steuerberatungsgellschaft mbH gegründet und suchen deshalb ein neues Kanzleilogo / Geschäftspapiere. Wir betreuen/beraten kleine Unternehmen und Privatpersonen aus der Region und haben derzeitig 14 Angestellte.
Aufgabenstellung
Das Design sollte in erster Linie seriös und nicht verspielt wirken. Einer vertrauensvollen Steuerberaterungskanzlei entsprechend. Dennoch sind wir auch für eine moderne Gestaltung offen.

```html
<!DOCTYPE html>
<html lang="de">
<head>
<meta charset="utf-8">
<title>Wimmler Steuerberatungsgesellschaft mbH – Geschäftsausstattung</title>
<link href="https://fonts.googleapis.com/css2?family=Open+Sans:wght@400;700&family=Oswald:wght@300;400;500;600&display=swap" rel="stylesheet">
<style>
:root{
  --backdrop:#2b3038;
  --paper:#ffffff;
  --teal:#1c7b8e;
  --navy:#0f3b4c;
  --ink:#2a2a2a;
  --muted:#4a4a4a;
}
*{margin:0;padding:0;box-sizing:border-box}
html,body{width:1200px;height:848px;overflow:hidden}
body{background:var(--backdrop);position:relative;font-family:"Open Sans",sans-serif}
.sheet{position:absolute;background:var(--paper);box-shadow:0 4px 14px rgba(0,0,0,.45)}
.corner{position:absolute;border-color:var(--teal);border-style:solid}
.corner--tr{top:0;right:0;border-width:0 0 2px 2px}
.corner--bl{bottom:0;left:0;border-width:2px 2px 0 0}

.brand{position:absolute;display:flex;align-items:center}
.brand__mark{border:2px solid var(--teal);flex:none}
.brand__text{display:flex;flex-direction:column;line-height:1}
.brand__name{font-family:"Oswald",sans-serif;font-weight:600;color:var(--navy);letter-spacing:.04em}
.brand__tagline{font-family:"Oswald",sans-serif;font-weight:300;color:var(--teal);letter-spacing:.03em}

/* letterhead */
.letter{left:172px;top:64px;width:509px;height:720px}
.letter .corner{width:29px;height:29px}
.letter .brand{left:30px;top:30px;gap:8px}
.letter .brand__mark{width:26px;height:26px}
.letter .brand__name{font-size:20px}
.letter .brand__tagline{font-size:7px;margin-top:2px}
.sender-line{position:absolute;left:55px;top:111px;font-size:5.6px;color:var(--teal);border-bottom:.6px solid var(--teal);padding-bottom:1px}
.recipient{position:absolute;left:55px;top:130px;font-size:8px;line-height:10.5px;color:var(--ink);font-style:normal}
.recipient .city{margin-top:10px}
.subject{position:absolute;left:55px;top:245px;font-size:7.6px;font-weight:700;color:var(--ink)}
.body-copy{position:absolute;left:55px;top:272px;width:276px;font-size:7.85px;line-height:9.25px;color:var(--muted)}
.body-copy p+p{margin-top:9px}
.closing{position:absolute;left:55px;top:505px;font-size:7.6px;color:var(--muted)}
.signature{position:absolute;left:55px;top:525px;width:108px;height:20px;background:linear-gradient(90deg,#ececec,#f6f6f6)}
.signer{position:absolute;left:55px;top:555px;font-size:7.6px;color:var(--muted)}
.footer{position:absolute;top:678px;left:0;width:100%;font-family:"Oswald",sans-serif;font-weight:400;font-size:6.6px;line-height:10.2px;letter-spacing:.08em;color:var(--navy)}
.footer__col{position:absolute}
.footer__col:nth-child(1){left:55px}
.footer__col:nth-child(2){left:174px}
.footer__col:nth-child(3){left:304px}

/* business cards */
.card{width:272px;height:176px}
.card .corner{width:26px;height:25px}
.card--front{left:768px;top:198px}
.card--back{left:766px;top:475px;width:275px;height:178px}
.card .brand{gap:11px}
.card .brand__mark{width:36px;height:36px;border-width:2.5px}
.card .brand__name{font-size:27px}
.card .brand__tagline{font-size:9.6px;margin-top:2px}
.card--front .brand{left:21px;top:20px}
.card--back .brand{left:47px;top:68px}
.contact{position:absolute;left:71px;top:78px;font-family:"Oswald",sans-serif;font-weight:300;font-size:8.6px;letter-spacing:.05em;color:var(--navy);line-height:11px}
.contact .name{color:var(--teal);font-weight:500;font-size:9.2px}
.contact .row{margin-top:3px}
.contact .label{color:var(--teal)}
.contact .dot{display:inline-block;width:3px;height:3px;background:var(--navy);vertical-align:middle;margin:0 4px}
.contact .web{color:var(--teal);font-weight:500;margin-top:4px}
</style>
</head>
<body>

<section class="sheet letter" aria-label="Briefbogen">
  <span class="corner corner--tr"></span>
  <span class="corner corner--bl"></span>
  <div class="brand">
    <span class="brand__mark"></span>
    <div class="brand__text">
      <span class="brand__name">Wimmler</span>
      <span class="brand__tagline">Steuerberatungsgesellschaft mbH</span>
    </div>
  </div>
  <p class="sender-line">Jonas Feldhuber, Lindenweg 14, 93301 Auental</p>
  <address class="recipient">
    Sabine Kerschl<br>Ahornstraße 27
    <div class="city">40210 Rheinfeld</div>
  </address>
  <h1 class="subject">Quidero molore, atatur sae. Nequat,</h1>
  <div class="body-copy">
    <p>Ur sit, imus, ipicatem voluptate eum re dolluptios sequosam, eum reritati am volor sapedissi quo blaboribust, sequass itasped igendi cus exerfer feruptas iusanda ndaest, qui omnis nus aut fugitinis quatur ad ullaut mostem quasperiae corem et aciatem illatin ciduntores quidis utemquam autemperae soluptiae lab illacescia solorum et fugiam ratatatus exerro blaciis samusam etur? Uga. Neque nam simi, nest, ommod essedios magnatia nossi aute nonsequam fugiaspis moluptas sed el int etur saepe nonsecatem excea noneceperrum ulligendit faccullores et lantur si ium at.Ota cuptae non ea de opta voles rem rae dolore ilia vellab isi blanis idit veribus auda alit labore desenis imenis que in con rehent, explat ped que volorum, autent, si tetur?</p>
    <p>Ihil ium restior ecepero reptistius es aborepe diatiunt dignis diciae voluptu ribearit, que nat aute et as maximus, qui blab iur aut volest, nonsequae odios doluptatiae velignimin perescia vent.<br>Pa voluptas expero corectur molest eaquid enda vidus verciis quodi te dit aliquid unturem poreper feratur? Quis aut rehenihilit et quam, eris et perorru mquamusa quo et untia volupie nisimoluptae esseribus cora doluptati doluptatur atisciumqui re pa quat aut lam solescia intiis et millabor sit odis et quos re sam, vendicientur abo. Equi totatus rest, nosam quodi omni doloriosam des ea nimpelique volo elendae dellign ihilitis solupta temporp orupta iuntia ipiste natibusapis volesedis reriori taerrup tatiberes nobitiur, sequi omnihillab id maximagnat omnimus dolo quunt, int aut earum lacit peliquunt iduciet, id que autemolum deruptati te non re.</p>
  </div>
  <p class="closing">Sincerely</p>
  <div class="signature" role="img" aria-label="Handschriftliche Unterschrift"></div>
  <p class="signer">Jonas Feldhuber</p>
  <footer class="footer">
    <div class="footer__col">Jonas Feldhuber<br>Lindenweg 14<br>93301 Auental</div>
    <div class="footer__col">T: 0947 / 508 210<br>F: 0947 / 508 219<br>info@wimmler-stb.de</div>
    <div class="footer__col">Donautal Bank eG<br>IBAN: DE6075091322<br>BIC: DTBKDE71AUE</div>
  </footer>
</section>

<section class="sheet card card--front" aria-label="Visitenkarte Vorderseite">
  <span class="corner corner--tr"></span>
  <span class="corner corner--bl"></span>
  <div class="brand">
    <span class="brand__mark"></span>
    <div class="brand__text">
      <span class="brand__name">Wimmler</span>
      <span class="brand__tagline">Steuerberatungsgesellschaft mbH</span>
    </div>
  </div>
  <div class="contact">
    <div class="name">Jonas Feldhuber</div>
    <div>Geschäftsführer</div>
    <div class="row">Lindenweg 14<span class="dot"></span>93301 Auental</div>
    <div class="row"><span class="label">T:</span> 0947 / 508 210 &nbsp; <span class="label">F:</span> 0947 / 508 218</div>
    <div>kontakt@wimmler-stb.de</div>
    <div class="web">www.wimmler-stb.de</div>
  </div>
</section>

<section class="sheet card card--back" aria-label="Visitenkarte Rückseite">
  <span class="corner corner--tr"></span>
  <span class="corner corner--bl"></span>
  <div class="brand">
    <span class="brand__mark"></span>
    <div class="brand__text">
      <span class="brand__name">Wimmler</span>
      <span class="brand__tagline">Steuerberatungsgesellschaft mbH</span>
    </div>
  </div>
</section>

</body>
</html>
```